Flyer for a Payroll and Bookkeeping Companmy

Need a brochure to highlight our costs and service to hand out to clients.

Please see attachments for more information.

It Service

```html
<!DOCTYPE html>
<html lang="en">
<head>
<meta charset="utf-8">
<title>Summit Ridge – Pricing Flyers</title>
<link href="https://fonts.googleapis.com/css2?family=Roboto:wght@300;400;700&family=Arimo:wght@400;700&family=Source+Sans+3:wght@400;600&display=swap" rel="stylesheet">
<style>
:root{
  --blue:#0b72bd;
  --blue-dark:#0a5f9e;
  --orange:#ee7d26;
  --brown:#8a3d14;
  --ink:#111;
  --grey-text:#555;
  --row-alt:#f4f5f6;
  --line:#333;
  --bg:#e9e9e9;
  --white:#fff;
}
*{box-sizing:border-box;margin:0;padding:0}
html,body{width:956px;height:1200px;overflow:hidden;background:var(--bg)}
.stage{position:absolute;left:0;top:0;width:1130px;height:1419px;transform:scale(.846);transform-origin:0 0}
.card{position:absolute;left:151px;width:850px;height:550px;background:var(--white);box-shadow:0 4px 14px rgba(0,0,0,.25);overflow:hidden}
.card--bookkeeping{top:117px}
.card--payroll{top:737px}

/* brand */
.brand{position:absolute;display:flex;align-items:center;gap:8px;font-family:"Source Sans 3",sans-serif;font-weight:600;color:var(--blue)}
.brand__dot{border-radius:50%;background:var(--orange)}
.card--bookkeeping .brand{right:36px;top:62px;font-size:22px}
.card--bookkeeping .brand__dot{width:14px;height:14px}
.card--payroll .brand{left:560px;top:100px;font-size:32px}
.card--payroll .brand__dot{width:20px;height:20px}

/* section title bar */
.title-bar{position:absolute;left:0;top:32px;width:333px;height:49px;background:var(--blue);clip-path:polygon(0 0,318px 0,333px 49px,0 49px);font-family:"Roboto",sans-serif;font-weight:400;color:var(--white);font-size:24px;line-height:49px;padding-left:34px}

/* pricing table */
.pricing{position:absolute;left:33px;top:109px;width:787px;border-collapse:collapse;font-family:"Arimo",sans-serif;color:var(--ink);table-layout:fixed}
.pricing col.service{width:242px}
.pricing td,.pricing th{border:1px solid var(--line);height:40.5px;text-align:center;vertical-align:middle}
.pricing tbody tr:nth-child(even) td{background:var(--row-alt)}
.pricing .service-name{text-align:right;padding-right:7px;font-weight:700;font-size:13px;line-height:1.1}
.pricing .service-name small{display:block;font-weight:400;font-size:10px}
.pricing thead th{border:none;padding:0}
.pricing .head-services{background:var(--blue);color:var(--white);font-weight:400;font-size:16px;border:1px solid var(--blue-dark)}
.tier{height:46px}
.tier__name{display:block;background:var(--brown);color:var(--white);font-size:12px;font-weight:400;height:14px;line-height:14px}
.tier__price{display:block;background:var(--orange);color:var(--white);font-size:24px;font-weight:400;height:32px;line-height:32px;border-left:1px solid rgba(255,255,255,.4)}
.qty{font-size:13px;font-weight:700;line-height:1}
.qty small{display:block;font-size:9px;font-weight:400}
.tick{display:block;margin:0 auto;width:16px;height:13px}
.freq{display:block;color:var(--orange);font-size:11px;font-weight:700;margin-top:2px}
.price-cell{font-size:13px}
.none{font-size:15px}

/* footer band */
.contact-band{position:absolute;left:0;bottom:0;width:850px;height:55px;background:var(--orange);display:flex;align-items:center;padding-left:33px;font-family:"Source Sans 3",sans-serif;color:var(--white);font-size:19.5px}
.contact{display:flex;align-items:center;gap:10px;margin-right:34px}
.contact svg{width:26px;height:26px}

/* payroll card */
.hero-photo{position:absolute;left:0;top:0;width:500px;height:483px;background:linear-gradient(135deg,#d9e0e3 0%,#eef1f2 40%,#c9d3d8 70%,#9eaeb8 100%);clip-path:polygon(0 0,425px 0,500px 483px,0 483px)}
.payroll-title{position:absolute;left:460px;width:390px;top:180px;text-align:center;font-family:"Roboto",sans-serif;font-weight:400;font-size:26px;color:var(--blue)}
.rate-box{position:absolute;left:460px;top:220px;width:390px;height:116px;background:var(--blue);clip-path:polygon(0 0,100% 0,100% 100%,15px 100%);color:var(--white);font-family:"Source Sans 3",sans-serif;font-weight:600;font-size:24.5px;line-height:33px;text-align:center;padding-top:8px;box-shadow:0 3px 6px rgba(0,0,0,.2)}
.terms{position:absolute;left:490px;width:350px;top:376px;text-align:center;font-family:"Source Sans 3",sans-serif;font-size:15px;line-height:19.5px;color:var(--grey-text)}
.terms .highlight{color:var(--orange)}
</style>
</head>
<body>
<svg width="0" height="0" style="position:absolute">
  <defs>
    <symbol id="tick" viewBox="0 0 16 13"><path d="M1 7l4.5 4.5L15 1.5" fill="none" stroke="#ee7d26" stroke-width="2.6" stroke-linecap="round" stroke-linejoin="round"/></symbol>
    <symbol id="icon-pin" viewBox="0 0 26 26"><circle cx="13" cy="13" r="12.5" fill="#fff"/><path d="M13 5.5a5.5 5.5 0 0 0-5.5 5.5c0 4 5.5 9.5 5.5 9.5s5.5-5.5 5.5-9.5A5.5 5.5 0 0 0 13 5.5z" fill="#ee7d26"/><circle cx="13" cy="11" r="2" fill="#fff"/></symbol>
    <symbol id="icon-phone" viewBox="0 0 26 26"><circle cx="13" cy="13" r="12.5" fill="#fff"/><circle cx="13" cy="13" r="9" fill="none" stroke="#ee7d26" stroke-width="1.5"/><path d="M10 8.5l2 2.5-1.2 1.5c.7 1.5 1.7 2.5 3.2 3.2l1.5-1.2 2.5 2-1.3 2c-3.5-.3-7.2-4-7.5-7.5z" fill="#ee7d26"/></symbol>
    <symbol id="icon-web" viewBox="0 0 26 26"><circle cx="13" cy="13" r="12.5" fill="#fff"/><g fill="none" stroke="#ee7d26" stroke-width="1.4"><circle cx="13" cy="13" r="8"/><ellipse cx="13" cy="13" rx="3.5" ry="8"/><path d="M5 13h16M6.5 9h13M6.5 17h13"/></g></symbol>
  </defs>
</svg>

<main class="stage">
  <section class="card card--bookkeeping">
    <h1 class="title-bar">BOOKKEEPING PRICING</h1>
    <div class="brand"><span class="brand__dot"></span>Summit Ridge</div>

    <table class="pricing">
      <colgroup><col class="service"><col><col><col><col></colgroup>
      <thead>
        <tr>
          <th class="head-services">SERVICES</th>
          <th class="tier"><span class="tier__name">Premium</span><span class="tier__price">$999</span></th>
          <th class="tier"><span class="tier__name">Entrepreneur</span><span class="tier__price">$599</span></th>
          <th class="tier"><span class="tier__name">Growth</span><span class="tier__price">$299</span></th>
          <th class="tier"><span class="tier__name">Start Up</span><span class="tier__price">$149</span></th>
        </tr>
      </thead>
      <tbody>
        <tr><td class="service-name">Employees</td>
          <td class="qty"><small>Around</small>10+</td><td class="qty"><small>Around</small>5-9</td><td class="qty"><small>Around</small>2-5</td><td class="qty"><small>Around</small>1-2</td></tr>
        <tr><td class="service-name">Transactions / Month</td>
          <td class="qty"><small>Up to</small>250</td><td class="qty"><small>Up to</small>150</td><td class="qty"><small>Up to</small>75</td><td class="qty"><small>Up to</small>50</td></tr>
        <tr><td class="service-name">Bookkeeping</td>
          <td><svg class="tick"><use href="#tick"/></svg><span class="freq">Weekly</span></td>
          <td><svg class="tick"><use href="#tick"/></svg><span class="freq">Weekly</span></td>
          <td><svg class="tick"><use href="#tick"/></svg><span class="freq">Monthly</span></td>
          <td><svg class="tick"><use href="#tick"/></svg><span class="freq">Quarterly</span></td></tr>
        <tr><td class="service-name">Financial Reports &amp; Review</td>
          <td><svg class="tick"><use href="#tick"/></svg><span class="freq">Monthly</span></td>
          <td><svg class="tick"><use href="#tick"/></svg><span class="freq">Monthly</span></td>
          <td><svg class="tick"><use href="#tick"/></svg><span class="freq">Monthly</span></td>
          <td><svg class="tick"><use href="#tick"/></svg><span class="freq">Quarterly</span></td></tr>
        <tr><td class="service-name">Support<small>(Phone and Chatly)</small></td>
          <td><svg class="tick"><use href="#tick"/></svg></td><td><svg class="tick"><use href="#tick"/></svg></td><td><svg class="tick"><use href="#tick"/></svg></td><td><svg class="tick"><use href="#tick"/></svg></td></tr>
        <tr><td class="service-name">Online Collaboration Portal<small>(CloudBox Files)</small></td>
          <td><svg class="tick"><use href="#tick"/></svg></td><td><svg class="tick"><use href="#tick"/></svg></td><td><svg class="tick"><use href="#tick"/></svg></td><td><svg class="tick"><use href="#tick"/></svg></td></tr>
        <tr><td class="service-name">Business Tax Return</td>
          <td><svg class="tick"><use href="#tick"/></svg></td><td><svg class="tick"><use href="#tick"/></svg></td><td class="price-cell">$799</td><td class="price-cell">$599</td></tr>
        <tr><td class="service-name">Bill Pay<small>(with Approval Process)</small></td>
          <td><svg class="tick"><use href="#tick"/></svg><span class="freq">$5 / Payment</span></td><td class="none">x</td><td class="none">x</td><td class="none">x</td></tr>
      </tbody>
    </table>

    <footer class="contact-band">
      <span class="contact"><svg><use href="#icon-pin"/></svg>2210 N Maple Ave, Riverton, UT 84065</span>
      <span class="contact"><svg><use href="#icon-phone"/></svg>555-014-2290</span>
      <span class="contact"><svg><use href="#icon-web"/></svg>SummitRidge.com</span>
    </footer>
  </section>

  <section class="card card--payroll">
    <div class="hero-photo" role="img" aria-label="Photo of a person at a bright office desk using a tablet with a stylus beside a keyboard and printed charts"></div>
    <div class="brand"><span class="brand__dot"></span>Summit Ridge</div>
    <h2 class="payroll-title">SIMPLIFIED PAYROLL PRICING</h2>
    <div class="rate-box">$25 per Payroll<br>+$5 per Employee<br>No Set Up Fees!</div>
    <p class="terms">Direct deposit only, add $20 per payroll<br>if you elect to have paper checks shipped to you.<br>Minimum charge of two payrolls per month.<br><span class="highlight">Cost per employee drops to $4 after 20 employees.</span></p>
    <footer class="contact-band">
      <span class="contact"><svg><use href="#icon-pin"/></svg>2210 N Maple Ave, Riverton, UT 84065</span>
      <span class="contact"><svg><use href="#icon-phone"/></svg>555-014-2290</span>
      <span class="contact"><svg><use href="#icon-web"/></svg>SummitRidge.com</span>
    </footer>
  </section>
</main>
</body>
</html>
```